Meridian Rest Supply Needs Business Card

Looking for a very nice looking business card. Creative but not extravagant. We sell beds and pillows across the U.S. and need something professional but catchy. I have attached the logo.

Name : Dale Fenwick
Title : President
Phone : (800) 417-2964
Email: sleep@quorvana.com
Website: www.quorvana.com

Can be single-sided or double-sided
horizontal or vertical

Can use Blues/Greys

Target Market(s)

Mass Market

Industry/Entity Type

Retail

Contact Information for Business Card

Name : Dale Fenwick
Title : President
Phone : (800) 417-2964
Email: sleep@quorvana.com
Website: www.quorvana.com

Requirements
Must have
• Clean, Modern, Smooth
• Can use Blues/Greys
• On the other side without the information - have something simple like www.quorvana.com or our logo
Nice to have
• Surprise me
Should not have
• Nothing crazy, nothing cluttered

```html
<!DOCTYPE html>
<html lang="en">
<head>
<meta charset="utf-8">
<title>Meridian Rest Supply – Business Card</title>
<link rel="stylesheet" href="https://fonts.googleapis.com/css2?family=Arimo:wght@400;700&family=Quicksand:wght@300;400&display=swap">
<style>
  :root {
    --sky: #35a4d6;
    --sky-deep: #1f89b6;
    --sky-dark: #175f80;
    --paper: #ffffff;
    --paper-shade: #e4e5e6;
    --logo-tint: #d6eef8;
    --stage: #e9eaeb;
  }
  html, body {
    margin: 0;
    width: 1200px;
    height: 1200px;
    overflow: hidden;
    background: var(--stage);
  }
  .canvas {
    position: relative;
    width: 1200px;
    height: 1200px;
  }
  .card {
    position: absolute;
    left: 206px;
    width: 784px;
    height: 454px;
    display: block;
  }
  .card--front { top: 84px; }
  .card--back { top: 630px; }
  .brand-name {
    font-family: "Quicksand", sans-serif;
    font-weight: 300;
  }
  .sans {
    font-family: "Arimo", Arial, sans-serif;
  }
</style>
</head>
<body>
<main class="canvas">

  <!-- Front side -->
  <svg class="card card--front" viewBox="0 0 784 454" aria-label="Card front">
    <rect class="front-base" width="784" height="454" fill="var(--sky)"/>
    <text class="brand-name" x="392" y="338" text-anchor="middle" font-size="96" fill="var(--paper)">quorvana</text>
    <rect class="front-band" x="0" y="384" width="784" height="34" fill="var(--sky-deep)"/>
    <g class="band-dots" fill="var(--paper)">
      <circle cx="29" cy="401" r="3.5"/>
      <circle cx="71" cy="401" r="4.5"/>
      <circle cx="112" cy="401" r="6"/>
      <circle cx="151" cy="401" r="8"/>
      <circle cx="192" cy="401" r="6.5"/>
      <circle cx="234" cy="401" r="10"/>
      <circle cx="539" cy="401" r="10"/>
      <circle cx="580" cy="401" r="7"/>
      <circle cx="620" cy="401" r="8"/>
      <circle cx="661" cy="401" r="6.5"/>
      <circle cx="703" cy="401" r="4.5"/>
      <circle cx="744" cy="401" r="3.5"/>
    </g>
    <text class="sans band-url" x="392" y="409" text-anchor="middle" font-size="22" fill="var(--paper)">www.quorvana.com</text>
  </svg>

  <!-- Back side -->
  <svg class="card card--back" viewBox="0 0 784 454" aria-label="Card back">
    <defs>
      <linearGradient id="paperGrad" x1="0.7" y1="0" x2="0.1" y2="1">
        <stop offset="0" stop-color="var(--paper)"/>
        <stop offset="1" stop-color="var(--paper-shade)"/>
      </linearGradient>
      <linearGradient id="panelGrad" x1="0" y1="0" x2="1" y2="0">
        <stop offset="0" stop-color="var(--sky-deep)"/>
        <stop offset="0.6" stop-color="#1d82ad"/>
        <stop offset="1" stop-color="var(--sky-dark)"/>
      </linearGradient>
    </defs>

    <rect class="back-base" width="784" height="454" fill="url(#paperGrad)"/>

    <path class="side-panel" d="M442 162 L784 162 L784 454 L514 454 L514 176 Z" fill="url(#panelGrad)"/>
    <path class="wave-edge" d="M0 424 C 260 420, 560 360, 784 288 L784 454 L0 454 Z" fill="var(--sky-deep)"/>
    <path class="wave" d="M0 432 C 260 428, 560 370, 784 300 L784 454 L0 454 Z" fill="var(--sky)"/>

    <rect class="name-tab" x="442" y="56" width="342" height="106" fill="var(--sky)"/>
    <text class="sans person-name" x="613" y="98" text-anchor="middle" font-size="32" font-weight="700" fill="var(--paper)">Dale Fenwick</text>
    <text class="sans person-title" x="613" y="131" text-anchor="middle" font-size="22" fill="var(--paper)">PRESIDENT</text>

    <g class="sans contact-lines" font-size="22" fill="var(--sky)" text-anchor="end">
      <text x="330" y="155">sleep@quorvana.com</text>
      <text x="330" y="239">(800) 417-2964</text>
      <text x="330" y="319">www.quorvana.com</text>
    </g>

    <g class="contact-icons" fill="none" stroke="var(--sky)" stroke-width="2.5">
      <!-- email -->
      <rect x="351" y="123" width="52" height="50"/>
      <rect x="362" y="138" width="30" height="21" stroke-width="2"/>
      <path d="M362 138 L377 151 L392 138" stroke-width="2"/>
      <!-- phone -->
      <rect x="351" y="207" width="52" height="50"/>
      <rect x="369" y="214" width="17" height="36" rx="3" stroke-width="2"/>
      <line x1="371" y1="219" x2="384" y2="219" stroke-width="1.5"/>
      <line x1="371" y1="244" x2="384" y2="244" stroke-width="1.5"/>
      <!-- web -->
      <rect x="351" y="287" width="52" height="50"/>
      <circle cx="377" cy="312" r="15" stroke-width="2"/>
      <ellipse cx="377" cy="312" rx="6.5" ry="15" stroke-width="1.8"/>
      <line x1="362" y1="312" x2="392" y2="312" stroke-width="1.8"/>
      <line x1="364" y1="304" x2="390" y2="304" stroke-width="1.5"/>
      <line x1="364" y1="320" x2="390" y2="320" stroke-width="1.5"/>
    </g>

    <text class="brand-name back-brand" x="774" y="428" text-anchor="end" font-size="46" fill="var(--logo-tint)">quorvana</text>
  </svg>

</main>
</body>
</html>
```